Creative website for a boutique software house*

We are looking for someone who will design a creative website for a software house which will correspond to our core values.
We are a client oriented, quality focused and problem solving aimed people who love challenging tasks.
We want our clients to feel safe and taken care of during working with us, we combine software knowledge with business experience in different fields. We have a holistic approach to every project treating it as our own and putting our whole hearts into our work and relations with clients.
We value transparency and trust.
We still don’t have the copywriter to write texts for us, if you’ll have any questions we are here to answer

Target Market(s)

Startups

Number of Pages Required

4 page

Requirements
Must have
• Sections:
who we are
what we do (offer)
why the client should chose us
our core values

```html
<!DOCTYPE html>
<html lang="en">
<head>
<meta charset="utf-8">
<title>Norvix — Boutique Software House</title>
<link href="https://fonts.googleapis.com/css2?family=Poppins:wght@400;500;600;700;800&family=Lato:wght@300;400;700&display=swap" rel="stylesheet">
<style>
:root{
  --brown:#7a4a1c;
  --brown-dark:#6b3f15;
  --text:#555049;
  --heading:#1c1c1c;
  --footer:#a98a6c;
  --wave-mid:#bea58a;
  --wave-light:#d8c9b7;
  --white:#ffffff;
}
*{margin:0;padding:0;box-sizing:border-box}
html,body{width:1200px;height:2927px;overflow:hidden}
body{position:relative;background:var(--white);font-family:'Lato',sans-serif;color:var(--text)}
.topbar{position:absolute;top:0;left:0;width:1200px;height:3px;background:var(--brown)}
.abs{position:absolute}

/* header */
.brand{left:111px;top:40px;display:flex;align-items:center;gap:10px;font-family:'Lato',sans-serif;font-size:32px;color:var(--brown);font-weight:400;letter-spacing:1px}
.brand-mark{width:30px;height:30px;border-radius:50%;background:var(--brown)}
.nav{left:341px;top:52px;display:flex;gap:37px;font-family:'Lato',sans-serif;font-weight:700;font-size:15px;color:#222}
.nav a{color:inherit;text-decoration:none;padding-bottom:10px}
.nav a.active{color:var(--brown);border-bottom:3px solid var(--brown)}
.btn{display:inline-flex;align-items:center;justify-content:center;gap:6px;background:var(--brown);color:var(--white);font-family:'Lato',sans-serif;font-weight:700;font-size:15px;border-radius:30px;text-decoration:none}
.login{left:971px;top:36px;width:117px;height:50px}

/* hero */
.hero-title{left:111px;top:196px;font-family:'Poppins',sans-serif;font-weight:700;font-size:46px;color:var(--brown);line-height:1}
.hero-sub{left:111px;top:248px;width:380px;font-family:'Poppins',sans-serif;font-weight:600;font-size:15.5px;color:#222;line-height:26px}
.get-started{left:110px;top:307px;width:152px;height:51px}
.hero-photo{left:616px;top:114px;width:420px;height:420px;border-radius:50%;background:radial-gradient(circle at 35% 45%,#7a4a22 0%,#c9c4bd 45%,#ece8e3 75%)}
.dots{left:110px;top:483px;display:flex;gap:4px}
.dots span{width:12px;height:12px;border-radius:50%;border:2px solid var(--brown)}
.dots span.on{background:var(--brown)}

/* values */
.value{width:134px;text-align:center}
.value-ring{width:134px;height:134px;border-radius:50%;border:5px solid var(--brown);display:flex;align-items:center;justify-content:center;background:rgba(255,255,255,.7)}
.value-name{margin-top:12px;font-family:'Poppins',sans-serif;font-weight:700;font-size:17px;color:var(--brown)}

/* who we are */
.who-photo{left:106px;top:865px;width:414px;height:414px;border-radius:50%;background:radial-gradient(circle at 60% 45%,#9a6a54 0%,#6b5b54 40%,#c7c9cc 80%)}
.section-title{font-family:'Poppins',sans-serif;font-weight:700;font-size:36px;color:var(--brown);line-height:1}
.section-title::after{content:"";display:block;width:88px;height:4px;background:var(--brown);margin-top:12px}
.who-title{left:612px;top:884px}
.body-text{font-family:'Lato',sans-serif;font-size:14.2px;letter-spacing:-0.1px;line-height:25.8px;text-align:justify;color:var(--text)}
.who-text{left:612px;top:948px;width:478px}
.who-text p+p{margin-top:25px}
.read-more{width:152px;height:51px}

/* what we do */
.what-title{left:0;width:1200px;top:1434px;text-align:center}
.what-title::after{margin:10px auto 0}
.card{top:1527px;width:315px;height:343px;background:var(--white);border-radius:8px;box-shadow:0 4px 30px rgba(0,0,0,.08);padding:46px 0 0 60px}
.card-icon{width:80px;height:80px}
.card h3{margin-top:22px;font-family:'Poppins',sans-serif;font-weight:600;font-size:17px;color:var(--brown)}
.card .lead{margin-top:8px;font-family:'Poppins',sans-serif;font-size:15.5px;color:#666}
.card ul{list-style:none;margin-top:6px}
.card li{display:flex;align-items:center;gap:12px;font-family:'Poppins',sans-serif;font-size:15.5px;color:#666;line-height:25.8px}
.card li.small{font-size:14px}
.bullet{width:13px;height:13px;flex:none}

/* why choose us */
.why-title{left:111px;top:2072px}
.why-text{left:111px;top:2136px;width:477px}
.why-photo{left:686px;top:2022px;width:360px;height:360px;border-radius:50%;background:radial-gradient(circle at 55% 35%,#2a8fd0 0%,#1b4f86 45%,#0f2747 85%)}

/* footer */
.footer-waves{left:0;top:2500px;width:1200px;height:120px}
.footer{left:0;top:2600px;width:1200px;height:327px;background:var(--footer);color:var(--white)}
.footer h4{position:absolute;top:60px;font-family:'Poppins',sans-serif;font-weight:600;font-size:16.5px;letter-spacing:.3px}
.footer-links{position:absolute;top:107px;list-style:none;font-family:'Lato',sans-serif;font-size:15.5px}
.footer-links li{line-height:34.5px}
.footer-links li::before{content:"» ";}
.social{position:absolute;left:572px;top:104px;list-style:none}
.social li{display:flex;align-items:center;gap:21px;height:55px;font-size:16px}
.social .dot{width:36px;height:36px;border-radius:50%;background:var(--white)}
.email{position:absolute;left:878px;top:110px;width:210px;height:36px;background:var(--white);border:1px solid #ccc;color:#555;font-size:13px;padding:10px}
.submit{position:absolute;left:878px;top:154px;width:86px;height:35px;background:var(--brown-dark);color:var(--white);font-family:'Poppins',sans-serif;font-weight:600;font-size:12.5px;display:flex;align-items:center;justify-content:center}
.footer-rule{position:absolute;left:111px;top:260px;width:977px;height:1px;background:rgba(255,255,255,.5)}
.copyright{position:absolute;left:0;width:1200px;top:277px;text-align:center;font-size:15px}
</style>
</head>
<body>
<div class="topbar"></div>

<header>
  <div class="abs brand"><span class="brand-mark"></span>norvix</div>
  <nav class="abs nav">
    <a class="active" href="#">HOME</a>
    <a href="#">WHO WE ARE</a>
    <a href="#">WHAT&nbsp; WE DO</a>
    <a href="#">WHY CHOOSE US</a>
    <a href="#">CONTACT US</a>
  </nav>
  <a class="abs btn login" href="#">
    <svg width="15" height="15" viewBox="0 0 16 16"><circle cx="8" cy="8" r="7" fill="none" stroke="#fff" stroke-width="1.6"/><circle cx="8" cy="6.3" r="2.4" fill="#fff"/><path d="M3.8 12.5c1-2 2.4-2.8 4.2-2.8s3.2.8 4.2 2.8" fill="#fff"/></svg>LOGIN</a>
</header>

<section class="hero">
  <h1 class="abs hero-title">NORVIX</h1>
  <p class="abs hero-sub">We combine software knowledge with business experience in different fields.</p>
  <a class="abs btn get-started" href="#">GET STARTED</a>
  <div class="abs hero-photo" role="img" aria-label="Photo of a woman working at a desktop computer showing the company presentation"></div>
  <div class="abs dots"><span class="on"></span><span></span><span></span><span></span></div>
</section>

<section class="values">
  <div class="abs value" style="left:111px;top:583px">
    <div class="value-ring"><svg width="70" height="50" viewBox="0 0 70 50" fill="none" stroke="#7a4a1c" stroke-width="2.5"><path d="M4 12h14l12 10 8-4 12 6h16"/><path d="M4 36h12l14 8 10-2 10-8h16"/><path d="M30 22l10 12"/></svg></div>
    <div class="value-name">INTEGRITY</div>
  </div>
  <div class="abs value" style="left:323px;top:626px">
    <div class="value-ring"><svg width="50" height="60" viewBox="0 0 50 60" fill="none" stroke="#7a4a1c" stroke-width="2.5"><circle cx="25" cy="24" r="14"/><path d="M19 40h12v8H19zM21 52h8"/></svg></div>
    <div class="value-name">INNOVATION</div>
  </div>
  <div class="abs value" style="left:533px;top:583px">
    <div class="value-ring"><svg width="70" height="56" viewBox="0 0 70 56" fill="none" stroke="#7a4a1c" stroke-width="2.5"><rect x="14" y="4" width="42" height="22" rx="4"/><circle cx="17" cy="40" r="5"/><circle cx="35" cy="40" r="5"/><circle cx="53" cy="40" r="5"/><path d="M9 54c1-5 15-5 16 0M27 54c1-5 15-5 16 0M45 54c1-5 15-5 16 0"/></svg></div>
    <div class="value-name">COMMITMENT</div>
  </div>
  <div class="abs value" style="left:743px;top:626px">
    <div class="value-ring"><svg width="56" height="60" viewBox="0 0 56 60" fill="none" stroke="#7a4a1c" stroke-width="2.5"><path d="M14 56V42C6 36 6 24 10 16 16 4 38 2 46 16c3 6 2 10 2 14l4 6h-6v10h-8v10"/><circle cx="30" cy="24" r="7"/></svg></div>
    <div class="value-name">CREATIVITY</div>
  </div>
  <div class="abs value" style="left:953px;top:583px">
    <div class="value-ring"><svg width="56" height="56" viewBox="0 0 56 56" fill="none" stroke="#7a4a1c" stroke-width="2.5"><circle cx="28" cy="28" r="24"/><path d="M18 40c0-12 8-22 20-24-2 12-8 20-20 24zM18 40l12-12"/></svg></div>
    <div class="value-name">GROWTH</div>
  </div>
</section>

<section class="who">
  <div class="abs who-photo" role="img" aria-label="Photo of a team working together at computers"></div>
  <h2 class="abs section-title who-title">WHO WE ARE</h2>
  <div class="abs body-text who-text">
    <p>We are a boutique software house (focused on the client, best quality of the service, lots of attention to the client and their product, customized approach etc) We are a client oriented, quality focused and problem solving aimed people who love challenging tasks.</p>
    <p>We want our clients to feel safe and taken care of during working with us, we combine software knowledge with business experience in different fields. We have a holistic approach to every project treating it as our own and putting our whole hearts into our work and relations with clients.</p>
  </div>
  <a class="abs btn read-more" style="left:612px;top:1196px" href="#">READ MORE
    <svg width="14" height="14" viewBox="0 0 14 14"><circle cx="7" cy="7" r="7" fill="#fff"/><path d="M5 3.5L8.5 7 5 10.5" stroke="#7a4a1c" stroke-width="2" fill="none"/></svg></a>
</section>

<section class="what">
  <h2 class="abs section-title what-title">WHAT WE DO</h2>

  <article class="abs card" style="left:111px">
    <svg class="card-icon" viewBox="0 0 80 80" fill="none" stroke="#7a4a1c" stroke-width="1.6"><circle cx="34" cy="12" r="8"/><circle cx="16" cy="28" r="7"/><circle cx="52" cy="32" r="7"/><path d="M34 20v38M16 35l16 18M52 39L36 55M4 56l14 10h34l24-10-6-4-18 6H30"/></svg>
    <h3>EARLY STARTUPS</h3>
    <ul>
      <li><svg class="bullet" viewBox="0 0 14 14"><circle cx="7" cy="7" r="7" fill="#7a4a1c"/><path d="M5 3.5L8.5 7 5 10.5" stroke="#fff" stroke-width="2" fill="none"/></svg>Building softwave</li>
      <li><svg class="bullet" viewBox="0 0 14 14"><circle cx="7" cy="7" r="7" fill="#7a4a1c"/><path d="M5 3.5L8.5 7 5 10.5" stroke="#fff" stroke-width="2" fill="none"/></svg>Mvp</li>
      <li><svg class="bullet" viewBox="0 0 14 14"><circle cx="7" cy="7" r="7" fill="#7a4a1c"/><path d="M5 3.5L8.5 7 5 10.5" stroke="#fff" stroke-width="2" fill="none"/></svg>Front end</li>
      <li><svg class="bullet" viewBox="0 0 14 14"><circle cx="7" cy="7" r="7" fill="#7a4a1c"/><path d="M5 3.5L8.5 7 5 10.5" stroke="#fff" stroke-width="2" fill="none"/></svg>Back end</li>
      <li><svg class="bullet" viewBox="0 0 14 14"><circle cx="7" cy="7" r="7" fill="#7a4a1c"/><path d="M5 3.5L8.5 7 5 10.5" stroke="#fff" stroke-width="2" fill="none"/></svg>Graphics</li>
    </ul>
  </article>

  <article class="abs card" style="left:443px">
    <svg class="card-icon" viewBox="0 0 80 80" fill="none" stroke="#7a4a1c" stroke-width="1.6"><circle cx="26" cy="30" r="18"/><path d="M26 18v12l8 6M22 8h8M26 8v4M52 20h12M56 30h12M52 40h12M6 62l12 8h26l14-8-4-4-14 6"/></svg>
    <h3>LATE STAGE STARTUPS</h3>
    <ul>
      <li><svg class="bullet" viewBox="0 0 14 14"><circle cx="7" cy="7" r="7" fill="#7a4a1c"/><path d="M5 3.5L8.5 7 5 10.5" stroke="#fff" stroke-width="2" fill="none"/></svg>Consulting</li>
      <li><svg class="bullet" viewBox="0 0 14 14"><circle cx="7" cy="7" r="7" fill="#7a4a1c"/><path d="M5 3.5L8.5 7 5 10.5" stroke="#fff" stroke-width="2" fill="none"/></svg>Implementing production</li>
      <li><svg class="bullet" viewBox="0 0 14 14"><circle cx="7" cy="7" r="7" fill="#7a4a1c"/><path d="M5 3.5L8.5 7 5 10.5" stroke="#fff" stroke-width="2" fill="none"/></svg>Restructuring codebases</li>
      <li><svg class="bullet" viewBox="0 0 14 14"><circle cx="7" cy="7" r="7" fill="#7a4a1c"/><path d="M5 3.5L8.5 7 5 10.5" stroke="#fff" stroke-width="2" fill="none"/></svg>Implement best engineer</li>
      <li><svg class="bullet" viewBox="0 0 14 14"><circle cx="7" cy="7" r="7" fill="#7a4a1c"/><path d="M5 3.5L8.5 7 5 10.5" stroke="#fff" stroke-width="2" fill="none"/></svg>Reviewing the code</li>
    </ul>
  </article>

  <article class="abs card" style="left:774px">
    <svg class="card-icon" viewBox="0 0 80 80" fill="none" stroke="#7a4a1c" stroke-width="1.6"><circle cx="24" cy="12" r="8"/><circle cx="14" cy="36" r="8"/><circle cx="34" cy="36" r="8"/><path d="M4 58l14 10h34l26-8-4-6-20 4H30"/></svg>
    <h3>CORPORATIONS</h3>
    <p class="lead">modernize their technology</p>
    <ul style="margin-top:10px">
      <li class="small"><svg class="bullet" viewBox="0 0 14 14"><circle cx="7" cy="7" r="7" fill="#7a4a1c"/><path d="M5 3.5L8.5 7 5 10.5" stroke="#fff" stroke-width="2" fill="none"/></svg>Lorem ipsum dolor sit</li>
      <li class="small"><svg class="bullet" viewBox="0 0 14 14"><circle cx="7" cy="7" r="7" fill="#7a4a1c"/><path d="M5 3.5L8.5 7 5 10.5" stroke="#fff" stroke-width="2" fill="none"/></svg>Amet, consectetur</li>
      <li class="small"><svg class="bullet" viewBox="0 0 14 14"><circle cx="7" cy="7" r="7" fill="#7a4a1c"/><path d="M5 3.5L8.5 7 5 10.5" stroke="#fff" stroke-width="2" fill="none"/></svg>Adipiscing elit, sed do</li>
      <li class="small"><svg class="bullet" viewBox="0 0 14 14"><circle cx="7" cy="7" r="7" fill="#7a4a1c"/><path d="M5 3.5L8.5 7 5 10.5" stroke="#fff" stroke-width="2" fill="none"/></svg>Eiusmod tempor</li>
    </ul>
  </article>
</section>

<section class="why">
  <h2 class="abs section-title why-title">WHY CHOOSE US</h2>
  <p class="abs body-text why-text">Lorem ipsum dolor sit amet, consectetur adipiscing elit, sed do eiusmod tempor incididunt ut labore et dolore magna aliqua. Ut enim ad minim veniam, quis nostrud exercitation ullamco laboris nisi ut aliquip ex ea commodo consequat. Duis aute irure dolor in reprehenderit in voluptate velit esse cillum dolore eu fugiat nulla pariatur. Excepteur sint occaecat cupidatat non proident, sunt in culpa qui officia</p>
  <a class="abs btn read-more" style="left:111px;top:2307px" href="#">READ MORE
    <svg width="14" height="14" viewBox="0 0 14 14"><circle cx="7" cy="7" r="7" fill="#fff"/><path d="M5 3.5L8.5 7 5 10.5" stroke="#7a4a1c" stroke-width="2" fill="none"/></svg></a>
  <div class="abs why-photo" role="img" aria-label="Photo of a laptop with a rising 2020 market chart"></div>
</section>

<svg class="abs footer-waves" viewBox="0 0 1200 120" preserveAspectRatio="none">
  <path d="M0 40C180 30 330 -5 600 60 800 5 1000 -10 1200 30V120H0Z" fill="var(--wave-light)"/>
  <path d="M0 50C200 10 420 10 620 60 700 85 900 110 1200 45V120H0Z" fill="var(--wave-mid)"/>
  <path d="M0 60C200 115 450 105 620 70 780 40 980 100 1200 85V120H0Z" fill="var(--footer)"/>
</svg>

<footer class="abs footer">
  <h4 style="left:110px">QUICK LINKS</h4>
  <ul class="footer-links" style="left:111px"><li>HOME</li><li>ABOUT</li><li>EVENTS</li><li>WHO WE ARE</li></ul>
  <ul class="footer-links" style="left:291px"><li>WHAT WE DO</li><li>WHY CHOOSE US</li><li>PRIVACY POLICY</li><li>RESOURCES</li></ul>
  <h4 style="left:571px">FOLLOW US</h4>
  <ul class="social">
    <li><span class="dot"></span>Circlebook</li>
    <li><span class="dot"></span>Chirper</li>
    <li><span class="dot"></span>Snapgram</li>
  </ul>
  <h4 style="left:877px">NEWSLETTER</h4>
  <div class="email">Email Address</div>
  <div class="submit">SUBMIT</div>
  <div class="footer-rule"></div>
  <p class="copyright">© Copyrights 2020 All Rights Reserved | Norvix.</p>
</footer>
</body>
</html>
```